Gourmet food company looking for a dazzling label for their premuim vinagrette dressings

Need a food label that will dazzle our customer and prove what a premium product we have. We make high end gourmet dressing for vegetables, fruit, meat, poultry and fish.

Our label will fit on a 250 mil Tolvenka Square bottle. Labels should be a 4x5 or even 5x5 depending on the design. Nutritionals, bar codes and company blurb will be supplied later. We really want to test you all's talent on this one and are very excited to see your renderings!

Our dressings are Champagne Pear Vinaigrette, White Balsmic Vinaigrette, Mojito Lime Vinaigrette, Creamy-Avacado Lime Vinaigrette, and Asian Sesame Vinaigrette. I hope these names will help you envision our product and kinda what we are looking for.
Updates

Thank you all so far for your renderings.I really don't want pictures if that helps. Our logo can be smaller and/or the name of the product bigger. Perhaps we can even redesign Velora and remove the leaf as I don't really care for what I see yet.So good luck and thanks Added Friday, August 19, 2016

I am still looking for that clean - elegant design for our product as our product is just that. If you look on the internet at vinegars and oils you will see many designs that are simple yet elegant. Creative lettering, bordering, color (can be black and white) and size will help accomplish this. So I invite you to use all your creativity and help me find just what we need.Many thanks Added Tuesday, August 23, 2016

Project Deadline Extended Reason: So many great designs coming in that I wanted a few extra days to tweek!Great job all Added Friday, August 26, 2016

Project Deadline Extended Reason: Very good designs thus far. We just need a few more days.Thanks Added Wednesday, August 31, 2016

Target Market(s)

High end grocery and specialty stores.

Our side panel on the label will say "At Velora we're fanatics for great flavors and are passionate about finding the best ingredients. From simple to elegant our products are "simply velora".

Industry/Entity Type

It Company

Font styles to use
Serif
Decorative
Script

Requirements
Must have
• A label that will draw the consumer to pick it up! Need something bold and elegant...
Nice to have
• Again, I really would like to have a label that pops. Since the bottle front is only about 2inches in width it will need some creativity. Would like something very simple and elegant.
• If the designer does not like the logo, please feel free to design without it!
Should not have
• Dark dark colors. We are selling dressing and we don't want any colors that may distort the contents.
• No stock photos for the front. I don't want our dressing to look like the others on the self. Brambleth Kitchen just uses lettering and a their packaging is eye catching

```html
<!DOCTYPE html>
<html lang="en">
<head>
<meta charset="utf-8">
<title>Velora Vinaigrette Labels</title>
<link rel="stylesheet" href="https://fonts.googleapis.com/css2?family=Marcellus&family=Pinyon+Script&family=UnifrakturMaguntia&family=Roboto:wght@400&display=swap">
<style>
  :root {
    --canvas: #ffffff;
    --frame: #9a9a9a;
    --cap: #333333;
    --glass: #e6e7e8;
    --glass-shine: #ffffff;
    --bottle-edge: #8a8a8a;
    --label-light: #fdf9dc;
    --label-mid: #efe3b0;
    --label-gold: #b79a5c;
    --dot-border: #e0424a;
    --ink: #3a2416;
    --leaf-green: #6f9a2c;
  }
  html, body {
    margin: 0;
    padding: 0;
    width: 1200px;
    height: 778px;
    overflow: hidden;
    background: var(--canvas);
  }
  .canvas {
    display: block;
    width: 1200px;
    height: 778px;
    box-sizing: border-box;
    border: 1px solid var(--frame);
  }
  .cap { fill: var(--cap); }
  .glass { fill: var(--glass); }
  .glass-shine { fill: var(--glass-shine); }
  .bottle-outline { fill: none; stroke: var(--bottle-edge); stroke-width: 1; }
  .label-border { fill: none; stroke: var(--dot-border); stroke-width: 1.2; stroke-dasharray: 2 2.5; }
  .brand-name {
    font-family: "Marcellus", serif;
    font-size: 48px;
    fill: var(--ink);
  }
  .tag-brand {
    font-family: "Marcellus", serif;
    font-size: 15px;
    fill: var(--ink);
  }
  .tagline {
    font-family: "Roboto", sans-serif;
    font-size: 10px;
    fill: var(--leaf-green);
  }
  .flavour-blackletter {
    font-family: "UnifrakturMaguntia", serif;
    font-size: 24px;
    fill: var(--ink);
  }
  .flavour-script {
    font-family: "Pinyon Script", cursive;
    font-size: 26px;
    fill: var(--ink);
  }
  .flavour-script.long { font-size: 22px; }
</style>
</head>
<body>
<svg class="canvas" viewBox="0 0 1460 946" width="1200" height="778" xmlns="http://www.w3.org/2000/svg">
  <defs>
    <linearGradient id="fill-champagne" x1="0" y1="0" x2="0" y2="1">
      <stop offset="0.25" stop-color="#fedd58"/>
      <stop offset="1" stop-color="#fdf3c6"/>
    </linearGradient>
    <linearGradient id="fill-balsamic" x1="0" y1="0" x2="0" y2="1">
      <stop offset="0.25" stop-color="#dcc59c"/>
      <stop offset="1" stop-color="#ebe0cb"/>
    </linearGradient>
    <linearGradient id="fill-mojito" x1="0" y1="0" x2="0" y2="1">
      <stop offset="0.25" stop-color="#d6d894"/>
      <stop offset="1" stop-color="#e9e9c9"/>
    </linearGradient>
    <linearGradient id="fill-avocado" x1="0" y1="0" x2="0" y2="1">
      <stop offset="0.25" stop-color="#b5c762"/>
      <stop offset="1" stop-color="#d4dfa3"/>
    </linearGradient>
    <linearGradient id="fill-sesame" x1="0" y1="0" x2="0" y2="1">
      <stop offset="0.55" stop-color="#603715"/>
      <stop offset="1" stop-color="#b8a597"/>
    </linearGradient>
    <linearGradient id="label-face" x1="0" y1="0" x2="0" y2="1">
      <stop offset="0" stop-color="var(--label-light)"/>
      <stop offset="0.45" stop-color="var(--label-mid)"/>
      <stop offset="1" stop-color="var(--label-gold)"/>
    </linearGradient>
    <linearGradient id="neck-tag" x1="0" y1="0" x2="0" y2="1">
      <stop offset="0" stop-color="#fdf9dc"/>
      <stop offset="0.55" stop-color="#f3e9bd"/>
      <stop offset="1" stop-color="#b89a5a"/>
    </linearGradient>
    <linearGradient id="flourish-tone" x1="0" y1="0" x2="1" y2="0">
      <stop offset="0" stop-color="#5a3b1e" stop-opacity="0"/>
      <stop offset="0.5" stop-color="#5a3b1e" stop-opacity="0.35"/>
      <stop offset="1" stop-color="#5a3b1e" stop-opacity="0"/>
    </linearGradient>

    <g id="bottle-glass">
      <rect class="cap" x="50" y="12" width="147" height="52"/>
      <rect class="glass" x="50" y="64" width="152" height="31" rx="14"/>
      <rect class="glass" x="67" y="90" width="114" height="146"/>
      <rect class="glass-shine" x="140" y="64" width="20" height="172"/>
    </g>
    <path id="bottle-body" d="M67,235 C67,278 0,300 0,362 L0,946 L248,946 L248,362 C248,300 181,278 181,235 Z"/>
    <path id="bottle-silhouette" d="M67,95 L67,235 C67,278 0,300 0,362 L0,946 M248,946 L248,362 C248,300 181,278 181,235 L181,95"/>

    <g id="neck-tag-strip">
      <rect x="103" y="12" width="34" height="255" fill="url(#neck-tag)" stroke="#c9b98a" stroke-width="0.6"/>
      <text class="tag-brand" transform="translate(126,238) rotate(-90)">Velora</text>
    </g>

    <g id="label-base">
      <rect x="22" y="425" width="205" height="257" fill="url(#label-face)"/>
      <rect class="label-border" x="30" y="433" width="189" height="241"/>
      <text class="brand-name" x="124.5" y="527" text-anchor="middle" textLength="150" lengthAdjust="spacingAndGlyphs">Velora</text>
      <text class="tagline" x="124.5" y="540" text-anchor="middle" textLength="160" lengthAdjust="spacingAndGlyphs">Thoughtfully Crafted Dressing</text>
      <rect x="74" y="628" width="101" height="34" rx="12" fill="url(#flourish-tone)" role="img" aria-label="Ornamental scroll flourish beneath the flavour name"/>
    </g>
  </defs>

  <g class="bottle" transform="translate(55,0)">
    <use href="#bottle-body" fill="url(#fill-champagne)"/>
    <use href="#bottle-glass"/>
    <use href="#bottle-silhouette" class="bottle-outline"/>
    <use href="#neck-tag-strip"/>
    <use href="#label-base"/>
    <text class="flavour-blackletter" x="124.5" y="592" text-anchor="middle" textLength="92" lengthAdjust="spacingAndGlyphs">Champagne</text>
    <text class="flavour-blackletter" x="124.5" y="617" text-anchor="middle" textLength="140" lengthAdjust="spacingAndGlyphs">Pear Vinaigrette</text>
  </g>

  <g class="bottle" transform="translate(336,0)">
    <use href="#bottle-body" fill="url(#fill-balsamic)"/>
    <use href="#bottle-glass"/>
    <use href="#bottle-silhouette" class="bottle-outline"/>
    <use href="#neck-tag-strip"/>
    <use href="#label-base"/>
    <text class="flavour-script" x="124.5" y="594" text-anchor="middle" textLength="130" lengthAdjust="spacingAndGlyphs">White Balsmic</text>
    <text class="flavour-script" x="124.5" y="622" text-anchor="middle" textLength="88" lengthAdjust="spacingAndGlyphs">Vinaigrette</text>
  </g>

  <g class="bottle" transform="translate(610,0)">
    <use href="#bottle-body" fill="url(#fill-mojito)"/>
    <use href="#bottle-glass"/>
    <use href="#bottle-silhouette" class="bottle-outline"/>
    <use href="#neck-tag-strip"/>
    <use href="#label-base"/>
    <text class="flavour-script" x="124.5" y="594" text-anchor="middle" textLength="110" lengthAdjust="spacingAndGlyphs">Mojito Lime</text>
    <text class="flavour-script" x="124.5" y="622" text-anchor="middle" textLength="88" lengthAdjust="spacingAndGlyphs">Vinaigrette</text>
  </g>

  <g class="bottle" transform="translate(884,0)">
    <use href="#bottle-body" fill="url(#fill-avocado)"/>
    <use href="#bottle-glass"/>
    <use href="#bottle-silhouette" class="bottle-outline"/>
    <use href="#neck-tag-strip"/>
    <use href="#label-base"/>
    <text class="flavour-script long" x="124.5" y="592" text-anchor="middle" textLength="170" lengthAdjust="spacingAndGlyphs">Creamy Avocado Lime</text>
    <text class="flavour-script long" x="124.5" y="617" text-anchor="middle" textLength="80" lengthAdjust="spacingAndGlyphs">Vinaigrette</text>
  </g>

  <g class="bottle" transform="translate(1157,0)">
    <use href="#bottle-body" fill="url(#fill-sesame)"/>
    <use href="#bottle-glass"/>
    <use href="#bottle-silhouette" class="bottle-outline"/>
    <use href="#neck-tag-strip"/>
    <use href="#label-base"/>
    <text class="flavour-script" x="124.5" y="594" text-anchor="middle" textLength="122" lengthAdjust="spacingAndGlyphs">Asian Sesame</text>
    <text class="flavour-script" x="124.5" y="622" text-anchor="middle" textLength="88" lengthAdjust="spacingAndGlyphs">Vinaigrette</text>
  </g>
</svg>
</body>
</html>
```